Business Card Design Project

We require a business card template to cover basic contact information - our company logo, names of employees, title, mobile and email.

Target Market(s)

Corporate

Industry/Entity Type

Business

Font styles to use
Sans Serif

Requirements
Nice to have
• Thinking it would be great just to have the logo taking up approximately half the space (so it goes as far across the top of the card as possible) and then contact details in the lower half of the card. Keen just to use only the two colours in the logo, on a white background.
Should not have
• No fussy drawings

```html
<!DOCTYPE html>
<html lang="en">
<head>
<meta charset="utf-8">
<title>Tidewell Developments — Business Card</title>
<link rel="stylesheet" href="https://fonts.googleapis.com/css2?family=Open+Sans:wght@400;600&display=swap">
<style>
  :root {
    --backdrop: #e4e5e7;
    --card-white: #f7f8f9;
    --card-blue: #7b9cc5;
    --brand-teal: #2ea3b2;
    --brand-blue: #4d78b9;
    --ink-blue: #3e6cb0;
  }
  * { margin: 0; padding: 0; box-sizing: border-box; }
  html, body {
    width: 1200px;
    height: 750px;
    overflow: hidden;
    background: var(--backdrop);
    font-family: "Open Sans", sans-serif;
  }
  .canvas {
    position: relative;
    width: 1200px;
    height: 750px;
  }
  .card {
    position: absolute;
    top: 237px;
    width: 480px;
    height: 276px;
    border-radius: 18px;
    overflow: hidden;
    box-shadow: 0 6px 18px rgba(0,0,0,0.12);
  }
  .card--back {
    left: 90px;
    background: var(--card-blue);
    display: flex;
    align-items: center;
    justify-content: center;
  }
  .card--front {
    left: 630px;
    background: var(--card-white);
  }
  .brand-name {
    font-weight: 600;
    color: var(--brand-teal);
    letter-spacing: -0.5px;
    white-space: nowrap;
  }
  .card--back .brand-name { font-size: 34px; }
  .card--front .brand-name {
    position: absolute;
    left: 32px;
    top: 58px;
    font-size: 30px;
  }
  .accent-bar {
    position: absolute;
    width: 14px;
  }
  .accent-bar--left {
    left: 0;
    top: 128px;
    height: 72px;
    background: var(--brand-blue);
  }
  .accent-bar--right {
    right: 0;
    top: 28px;
    height: 64px;
    background: var(--brand-teal);
  }
  .holder-name {
    position: absolute;
    left: 32px;
    top: 150px;
    font-size: 19px;
    color: var(--ink-blue);
  }
  .contact-list {
    position: absolute;
    right: 34px;
    top: 96px;
    list-style: none;
    font-size: 13px;
    line-height: 19px;
    color: var(--brand-teal);
  }
  .website {
    position: absolute;
    right: 70px;
    bottom: 40px;
    font-size: 16px;
    color: var(--ink-blue);
  }
</style>
</head>
<body>
<main class="canvas">
  <section class="card card--back" aria-label="Card back">
    <span class="brand-name">Tidewell Developments</span>
  </section>

  <section class="card card--front" aria-label="Card front">
    <span class="brand-name">Tidewell Developments</span>
    <span class="accent-bar accent-bar--left"></span>
    <span class="accent-bar accent-bar--right"></span>
    <p class="holder-name">YOUR NAME</p>
    <ul class="contact-list">
      <li>XXXXXX XXXXXXX XXXXXXX</li>
      <li>PH : 455-555-555</li>
      <li>EMAIL : YOURMAIL@YOUR.COM</li>
    </ul>
    <p class="website">WWW.YOURSITE.COM</p>
  </section>
</main>
</body>
</html>
```